Innovative Healthcare Technology Company needs a Business Card Design

We are in need of an innovative business card design for a new healthcare software company called "Brightwell Harbor Systems". We develop software that creates medical assessment applications and mobile e-learning prevention services to reduce risk behaviors in adolescent and young adults. Our initial product, the "MERIDIAN App", conducts a tailored sexual risk assessment and provides a doctor with an insightful patient report to improve sexual risk counseling and ultimately reduce unintended pregnancy, STDs, etc.

We would like the design to incorporate our logo and branding colors (attached) in an innovative and creative manner. The final design should communicate professionalism and healthcare innovation. Our tag line is "prevention is the solution" (doesn't necessarily need to be included) and our target audience is doctors, medical directors, and medical business administrators. Please visit our website for additional info ourlantrixhub.com. Be creative and we look forward to seeing your designs!

Target Market(s)

healthcare - doctors, medical directors and medical business administrators

Industry/Entity Type

Healthcare

Contact Information for Business Card

We would like the design to incorporate our logo and branding colors (attached) in an innovative and creative manner. The final design should communicate professionalism and healthcare innovation. Our tag line is "prevention is the solution" (doesn't necessarily need to be included)

Font styles to use
Other font styles liked:
• quicksand

Requirements
Must have
• our logo and brand colors
• Name, (Joan Ferraventi, PhD)
• Email (drjoan@ourlantrixhub.com)
• phone (555.213.8870)
• Website (ourlantrixhub.com)
Should not have
• cartoon look

```html
<!DOCTYPE html>
<html lang="en">
<head>
<meta charset="utf-8">
<title>Brightwell Harbor Systems — Business Card</title>
<link rel="stylesheet" href="https://fonts.googleapis.com/css2?family=Quicksand:wght@400;500;600&display=swap">
<style>
  :root {
    --brand-blue: #1f4d7d;
    --brand-green: #6ea68b;
    --brand-gray: #8d9196;
    --paper: #ffffff;
    --ink: #1f4d7d;
    --backdrop: #e9ebee;
    --photo-light: #e8eef2;
    --photo-mid: #c9d6df;
    --photo-deep: #a9bccb;
  }
  * { box-sizing: border-box; margin: 0; padding: 0; }
  html, body { width: 1200px; height: 1000px; overflow: hidden; }
  body {
    background: var(--backdrop);
    font-family: "Quicksand", sans-serif;
    color: var(--ink);
  }
  .cards {
    position: absolute; inset: 0;
    display: flex; align-items: center; justify-content: center; gap: 60px;
  }
  .card {
    position: relative;
    width: 525px; height: 300px;
    background: var(--paper);
    box-shadow: 0 6px 18px rgba(0,0,0,.12);
    overflow: hidden;
  }

  /* Brand lockup */
  .brand { display: flex; align-items: center; gap: 10px; }
  .brand-square { width: 22px; height: 22px; background: var(--brand-blue); flex: none; }
  .brand-name { font-weight: 500; color: var(--brand-blue); line-height: 1.1; }

  /* Front */
  .front .brand { position: absolute; left: 34px; top: 30px; }
  .front .brand-name { font-size: 19px; }
  .contact-list {
    position: absolute; left: 34px; top: 84px;
    list-style: none; font-size: 14px; font-weight: 500;
  }
  .contact-list li { display: flex; align-items: center; gap: 9px; height: 23px; }
  .contact-icon { width: 15px; height: 15px; flex: none; }
  .person-name {
    position: absolute; right: 40px; top: 150px;
    font-size: 21px; font-weight: 500;
  }
  .web-band {
    position: absolute; left: 0; right: 0; bottom: 24px; height: 60px;
    background: var(--brand-blue);
    display: flex; align-items: center; padding-left: 60px;
  }
  .web-band .url { color: var(--paper); font-size: 15px; font-weight: 500; }

  /* Back */
  .photo-field {
    position: absolute; inset: 14px;
    background: linear-gradient(135deg, var(--photo-light) 0%, var(--photo-mid) 45%, var(--photo-deep) 75%, var(--photo-light) 100%);
  }
  .photo-grid { position: absolute; inset: 14px; }
  .back .brand-panel {
    position: absolute; right: 14px; top: 120px;
    width: 285px; height: 92px;
    background: var(--paper);
    display: flex; align-items: center; padding-left: 22px;
  }
  .back .brand-name { font-size: 21px; }
</style>
</head>
<body>
<main class="cards">

  <section class="card front" aria-label="Business card front">
    <div class="brand">
      <span class="brand-square"></span>
      <span class="brand-name">Brightwell Harbor Systems</span>
    </div>

    <ul class="contact-list">
      <li>
        <svg class="contact-icon" viewBox="0 0 16 16" aria-hidden="true">
          <rect width="16" height="16" rx="2" fill="#1f4d7d"/>
          <path d="M5 3.5l1.6 2.3-1 1a6 6 0 0 0 3.6 3.6l1-1 2.3 1.6-.8 1.6c-3.9-.4-7-3.5-7.4-7.4z" fill="#fff"/>
        </svg>
        555.213.8870
      </li>
      <li>
        <svg class="contact-icon" viewBox="0 0 16 16" aria-hidden="true">
          <rect width="16" height="16" rx="2" fill="#6ea68b"/>
          <rect x="5" y="2.5" width="6" height="11" rx="1" fill="none" stroke="#fff" stroke-width="1.3"/>
          <circle cx="8" cy="11.3" r=".8" fill="#fff"/>
        </svg>
        555.213.8870
      </li>
      <li>
        <svg class="contact-icon" viewBox="0 0 16 16" aria-hidden="true">
          <rect width="16" height="16" rx="2" fill="#8d9196"/>
          <rect x="3" y="4.5" width="10" height="7" fill="none" stroke="#fff" stroke-width="1.2"/>
          <path d="M3 4.5l5 4 5-4" fill="none" stroke="#fff" stroke-width="1.2"/>
        </svg>
        drjoan@ourlantrixhub.com
      </li>
    </ul>

    <p class="person-name">Joan Ferraventi, PhD</p>

    <div class="web-band"><span class="url">ourlantrixhub.com</span></div>
  </section>

  <section class="card back" aria-label="Business card back">
    <div class="photo-field" role="img" aria-label="Photo collage of a physician in a white coat with a stethoscope holding a tablet"></div>
    <svg class="photo-grid" viewBox="0 0 497 272" preserveAspectRatio="none" aria-hidden="true">
      <g stroke="#ffffff" stroke-width="4">
        <line x1="95" y1="0" x2="95" y2="272"/>
        <line x1="190" y1="0" x2="190" y2="272"/>
        <line x1="290" y1="0" x2="290" y2="272"/>
        <line x1="395" y1="0" x2="395" y2="272"/>
        <line x1="0" y1="68" x2="497" y2="68"/>
        <line x1="0" y1="204" x2="497" y2="204"/>
      </g>
    </svg>
    <div class="brand-panel">
      <div class="brand">
        <span class="brand-square"></span>
        <span class="brand-name">Brightwell Harbor Systems</span>
      </div>
    </div>
  </section>

</main>
</body>
</html>
```